依頼詳細
新しい新聞店の形を目指しているので「シンプル」でありながら「洗練」された「かっこいい」デザインを希望します。
役員用は2社分の情報を記載のため情報量が多くなります。
詳細とロゴデータを添付します。
記載項目
表面:ロゴ、店名、役職、名前、携帯、アドレス2つ、URL、法人名・住所・電話・FAX ×2社分
希望イメージ
シンプル 複雑
単色 カラフル
暗い 明るい
日常 高級
遊び心 厳粛
未来的 伝統的
女性的 男性的
希望する色
赤系、青系、水色系、緑系、黄・オレンジ系、紫系
納品ファイル
• 高解像度JPG (.jpg)
• イラストレーター形式 (.ai)
• フォトショップ形式 (.psd)
• PNG形式 (.png)
補足説明
■ 選んだ理由

たくさんのご提案いただきありがとうございました。
選考には大変迷いましたが多い情報をうまくまとめていただき、ロゴもうまく活用していただきイメージ通りでしたので選ばせていただきました。大変気に入りました。

■ 提案者全員のお礼・コメント

この度は当社名刺デザインコンペにご提案いただき誠にありがとうございました。
どの作品も素晴らしく選考には大変迷いました。またご縁がありましたらよろしくお願いいたします。

```html
<!DOCTYPE html>
<html lang="ja">
<head>
<meta charset="utf-8">
<title>森川新聞店 名刺</title>
<link rel="stylesheet" href="https://fonts.googleapis.com/css2?family=Noto+Sans+JP:wght@400;500;700&family=Noto+Serif+JP:wght@500;700&display=swap">
<style>
:root{
  --stage:#3a3a3c;
  --paper:#ffffff;
  --ink:#222222;
  --ink-soft:#555555;
  --rule:#c8c8c8;
  --band-deep:#0b4aa2;
  --band-light:#3aa8ea;
  --accent-orange:#f39a1e;
  --accent-red:#d7261e;
  --brand-blue:#1c5fb4;
}
*{margin:0;padding:0;box-sizing:border-box}
html,body{width:720px;height:1200px;overflow:hidden;background:var(--stage)}
body{font-family:"Noto Sans JP",sans-serif;color:var(--ink);position:relative}
.card{position:absolute;left:40px;width:640px;height:340px;background:var(--paper);box-shadow:0 6px 16px rgba(0,0,0,.45)}
.card--executive{top:40px}
.card--manager-a{top:420px}
.card--manager-b{top:800px}

.brand{position:absolute;left:34px;top:50px;width:250px;text-align:center}
.brand__mark{display:block;width:46px;height:46px;margin:0 auto 10px;background:var(--accent-orange)}
.brand__name{font-family:"Noto Serif JP",serif;font-weight:700;font-size:34px;letter-spacing:2px;color:var(--brand-blue);line-height:1.2}
.brand__branch{margin-top:4px;font-size:11px;font-weight:700;color:var(--accent-red)}

.person{position:absolute;left:330px;top:30px}
.person__role{font-size:11px;color:var(--ink-soft)}
.person__name{font-family:"Noto Serif JP",serif;font-weight:500;font-size:28px;letter-spacing:6px;line-height:1.3;margin-bottom:6px}
.person__contact{font-size:10.5px;line-height:1.55;color:var(--ink-soft)}

.divider{position:absolute;height:1px;background:var(--rule)}
.card--executive .divider{left:30px;right:30px;top:172px}
.card--manager-a .divider,.card--manager-b .divider{left:330px;right:30px;top:160px}

.office{position:absolute;font-size:10px;line-height:1.6;color:var(--ink-soft)}
.office__center{font-weight:700;color:var(--accent-red);font-size:11px}
.office__company{font-weight:700;color:var(--ink);font-size:12.5px}
.card--executive .office--east{left:34px;top:182px}
.card--executive .office--west{left:330px;top:182px}
.card--manager-a .office,.card--manager-b .office{left:330px;top:172px}

.band{position:absolute;left:0;right:0;bottom:0;height:48px;background:linear-gradient(90deg,var(--band-deep),var(--band-light));border-top:3px solid var(--accent-orange)}
.band__url{display:block;text-align:center;color:#fff;font-size:11px;letter-spacing:.5px;line-height:45px}
</style>
</head>
<body>

<section class="card card--executive">
  <div class="brand">
    <span class="brand__mark"></span>
    <div class="brand__name">森川新聞店</div>
  </div>
  <div class="person">
    <div class="person__role">専務</div>
    <div class="person__name">森川 浩一郎</div>
    <div class="person__contact">Mobile. 090-1234-5678<br>Mail. koichiro@morikawa-news.example<br>office@morikawa-news.example</div>
  </div>
  <div class="divider"></div>
  <div class="office office--east">
    <div class="office__center">東原センター</div>
    <div class="office__company">有限会社モリネットワークサービス</div>
    <div>〒300-0051 東原県中央市山の手1-2-18</div>
    <div>Tel. 0120-22-2567 ／ Fax. 0120-22-3750</div>
  </div>
  <div class="office office--west">
    <div class="office__center">西野センター</div>
    <div class="office__company">株式会社森川新聞販売</div>
    <div>〒300-2705 東原県西野市南郷屋2-123-3</div>
    <div>Tel. 0120-36-0137 ／ Fax. 0120-37-0137</div>
  </div>
  <div class="band"><span class="band__url">https://morikawa-news.example</span></div>
</section>

<section class="card card--manager-a">
  <div class="brand">
    <span class="brand__mark"></span>
    <div class="brand__name">森川新聞店</div>
    <div class="brand__branch">東原センター</div>
  </div>
  <div class="person">
    <div class="person__role">店長</div>
    <div class="person__name">苗字 名前</div>
    <div class="person__contact">Mobile. 090-1234-5678</div>
  </div>
  <div class="divider"></div>
  <div class="office">
    <div class="office__center">東原センター</div>
    <div class="office__company">有限会社モリネットワークサービス</div>
    <div>〒300-0051 東原県中央市山の手1-2-18</div>
    <div>Tel. 0120-22-2567 ／ Fax. 0120-22-3750</div>
  </div>
  <div class="band"><span class="band__url">https://morikawa-news.example</span></div>
</section>

<section class="card card--manager-b">
  <div class="brand">
    <span class="brand__mark"></span>
    <div class="brand__name">森川新聞店</div>
    <div class="brand__branch">西野センター</div>
  </div>
  <div class="person">
    <div class="person__role">店長</div>
    <div class="person__name">苗字 名前</div>
    <div class="person__contact">Mobile. 090-1234-5678</div>
  </div>
  <div class="divider"></div>
  <div class="office">
    <div class="office__center">西野センター</div>
    <div class="office__company">株式会社森川新聞販売</div>
    <div>〒300-2705 東原県西野市南郷屋2-123-3</div>
    <div>Tel. 0120-36-0137 ／ Fax. 0120-37-0137</div>
  </div>
  <div class="band"><span class="band__url">https://morikawa-news.example</span></div>
</section>

</body>
</html>
```